L.M.T. Penrow

I am an indie author and already have a Facebook page. However, I would like it to be more professional and look less like a private Facebook page.

```html
<!DOCTYPE html>
<html lang="en">
<head>
<meta charset="utf-8">
<title>L.M.T. Penrow – Author Cover</title>
<link href="https://fonts.googleapis.com/css2?family=Oswald:wght@500;700&family=Open+Sans:wght@300;600&family=Great+Vibes&display=swap" rel="stylesheet">
<style>
  :root {
    --page-bg: #e9e9e9;
    --navy-deep: #061a4a;
    --navy-mid: #0b3a8c;
    --navy-glow: #1a5bc0;
    --gold: #c8b35a;
    --yellow: #f1d43c;
    --white: #ffffff;
    --frame-line: rgba(160, 190, 240, 0.45);
  }
  * { box-sizing: border-box; margin: 0; padding: 0; }
  html, body { width: 1200px; height: 1200px; overflow: hidden; background: var(--page-bg); }
  .canvas { position: relative; width: 1200px; height: 1200px; }

  .cover {
    position: absolute; left: 40px; top: 387px; width: 1120px; height: 426px;
    background: radial-gradient(ellipse at 62% 55%, var(--navy-glow) 0%, var(--navy-mid) 40%, var(--navy-deep) 100%);
    box-shadow: 0 4px 10px rgba(0,0,0,0.25);
    overflow: hidden;
  }
  .cover-frame { position: absolute; inset: 13px; border: 1px solid var(--frame-line); }

  .author-block { position: absolute; left: 30px; top: 0; width: 470px; height: 100%; }
  .author-block > * { position: absolute; left: 0; width: 100%; text-align: center; white-space: nowrap; }
  .author-name {
    top: 100px; font-family: "Oswald", sans-serif; font-weight: 700; font-size: 68px;
    line-height: 76px; color: var(--gold);
  }
  .author-role {
    top: 188px; font-family: "Open Sans", sans-serif; font-weight: 300; font-size: 32px;
    line-height: 40px; color: var(--white);
  }
  .tagline {
    top: 241px; font-family: "Oswald", sans-serif; font-weight: 500; font-size: 24px;
    line-height: 36px; color: var(--yellow); text-transform: uppercase;
  }
  .stores { top: 338px; display: flex; justify-content: center; gap: 14px; }
  .store {
    display: flex; align-items: center; gap: 5px;
    font-family: "Open Sans", sans-serif; font-weight: 600; font-size: 12px; line-height: 26px; color: var(--white);
  }
  .store-mark { width: 24px; height: 24px; background: var(--white); border-radius: 3px; }

  .book-title {
    position: absolute; left: 545px; top: 14px;
    font-family: "Great Vibes", cursive; font-size: 82px; color: var(--gold);
    transform: rotate(-6deg);
  }

  .art { position: absolute; }
  .art-tablet {
    left: 548px; top: 134px; width: 163px; height: 238px; border-radius: 8px;
    background: linear-gradient(160deg, #f4f4f4 0 6%, #c76a2a 20%, #f0a53a 50%, #3a2418 85%, #f4f4f4 94%);
  }
  .art-phone {
    left: 723px; top: 213px; width: 79px; height: 158px; border-radius: 8px;
    background: linear-gradient(160deg, #f4f4f4 0 8%, #c76a2a 22%, #f0a53a 50%, #3a2418 82%, #f4f4f4 92%);
  }
  .art-book {
    left: 826px; top: 50px; width: 250px; height: 340px; border-radius: 3px;
    background: linear-gradient(170deg, #b65a32 0%, #e39b4a 35%, #f3c24a 50%, #2b1e1a 80%, #0e0c10 100%);
    transform: skewY(-8deg);
  }
</style>
</head>
<body>
<main class="canvas">
  <section class="cover">
    <div class="cover-frame"></div>

    <div class="author-block">
      <h1 class="author-name">L.M.T. PENROW</h1>
      <p class="author-role">Author of Suspense</p>
      <p class="tagline">Letting Celeste into his<br>house is a big mistake...</p>
      <div class="stores">
        <span class="store"><span class="store-mark"></span>Quillory</span>
        <span class="store"><span class="store-mark"></span>Pagevane</span>
        <span class="store"><span class="store-mark"></span>Tomewick</span>
        <span class="store"><span class="store-mark"></span>Shelvaro</span>
      </div>
    </div>

    <div class="art art-tablet" role="img" aria-label="Tablet showing the Strata ebook cover"></div>
    <div class="art art-phone" role="img" aria-label="Phone showing the Strata ebook cover"></div>
    <div class="art art-book" role="img" aria-label="Paperback copy of Strata by L.M.T. Penrow"></div>

    <p class="book-title">Strata</p>
  </section>
</main>
</body>
</html>
```